Bright Summit Web Design

I am starting a new company that will provide LIFE COACHING services - I have tried to design a website, but it's too complicated. Right now, it's just me - I'm the only person that will provide services through the website - I have used makerhive to purchase a logo (see below). I want to be able to update the website myself, but need a template - basic design. Because I am not technologically savvy enough to explain in words - I basically want to have a website that will provide basic information about my services (coaching), a page about me and my background, hopefully scheduling possibilities, and testimonials — also a page for writing/blogs. I bought a website through NetBarn - so when I have a template, I guess I”d use that - but maybe I’ll need to work with a designer to actually get it up on the internet. I have a head shot that I’ll upload, too.
Clients from the independent (private school) world - teachers, administrators
4 page

```html
<!DOCTYPE html>
<html lang="en">
<head>
<meta charset="utf-8">
<title>Bright Summit Coaching</title>
<link href="https://fonts.googleapis.com/css2?family=Cormorant+Garamond:wght@500;600&family=Jost:wght@400;500;600&display=swap" rel="stylesheet">
<style>
:root{
  --green:#03a98d;
  --ink:#1b1b1b;
  --text:#5a5a5a;
  --mint:#e6f6f3;
  --white:#ffffff;
  --line:#e8e8e8;
}
*{box-sizing:border-box;margin:0;padding:0}
html,body{width:1200px;height:4954px;overflow:hidden;background:var(--white)}
body{position:relative;font-family:'Jost',sans-serif;color:var(--text)}
.abs{position:absolute}
.serif{font-family:'Cormorant Garamond',serif;color:var(--ink);font-weight:600;line-height:1.15}
.label{font-size:12px;font-weight:500;color:var(--green);text-transform:uppercase;letter-spacing:.3px}
.btn{position:absolute;display:flex;align-items:center;justify-content:center;font-size:12px;font-weight:600;text-transform:uppercase;letter-spacing:.3px}
.btn-dark{background:var(--ink);color:var(--white)}
.btn-outline{border:2px solid var(--ink);color:var(--ink)}
.link{font-size:11px;font-weight:500;color:var(--green);text-transform:uppercase;border-bottom:1px solid var(--green);padding-bottom:2px}
.ph{position:absolute}

/* header + hero */
.hero{position:absolute;left:0;top:0;width:1200px;height:683px;background:linear-gradient(180deg,#ffffff 0%,#eef9f7 30%,var(--mint) 100%)}
.brand{position:absolute;left:87px;top:52px;display:flex;align-items:center;gap:10px;font-size:17px;font-weight:500;color:var(--ink);letter-spacing:.5px}
.brand i{width:30px;height:30px;border:2px solid var(--green);border-radius:50%}
.nav{position:absolute;top:53px;font-size:12px;color:#444}
.nav.active{color:var(--green)}
.dot{position:absolute;top:56px;width:10px;height:10px;background:var(--green);border-radius:2px}
.hero h1{position:absolute;left:513px;top:245px;font-size:60px;width:640px}
.hero p{position:absolute;left:513px;top:416px;width:580px;font-size:13px;line-height:1.6}

/* story */
.story h2{font-size:46px}
.story p{font-size:13px;line-height:1.75;width:490px}

/* services */
.band-green{position:absolute;left:0;top:1385px;width:1200px;height:475px;background:var(--green)}
.card{position:absolute;background:var(--white);box-shadow:0 6px 22px rgba(0,0,0,.07)}
.svc-title{font-size:24px}
.small{font-size:11.5px;line-height:1.75}
.tag{position:absolute;top:26px;right:26px;background:var(--green);color:var(--white);font-size:11px;padding:4px 14px;border-radius:14px}

/* testimonials */
.band-mint{position:absolute;left:0;top:2798px;width:1200px;height:558px;background:var(--mint)}
.quote{position:absolute;background:var(--white);padding:28px 28px;width:237px;height:243px;font-size:12.5px;line-height:1.75}
.quote:after{content:"";position:absolute;left:40px;bottom:-12px;border:12px solid transparent;border-bottom:0;border-top-color:var(--white)}
.avatar{position:absolute;width:58px;height:58px;border-radius:50%;background:linear-gradient(135deg,#c9b2a0,#6d5548)}

/* blog */
.badge{position:absolute;width:60px;height:62px;background:var(--green);color:var(--white);text-align:center;font-size:17px;font-weight:600;line-height:1.1;padding-top:9px}
.badge span{font-size:14px;display:block}

/* footer */
.foot-link{position:absolute;font-size:11.5px;color:#444;text-transform:uppercase}
.social{position:absolute;top:4645px;width:40px;height:40px;border:1.5px solid var(--green);border-radius:50%}
</style>
</head>
<body>

<section class="hero">
  <div class="brand"><i></i>BRIGHT SUMMIT</div>
  <span class="nav active" style="left:438px">Home</span>
  <span class="nav" style="left:513px">About Me</span>
  <span class="nav" style="left:611px">My Services</span>
  <span class="nav" style="left:721px">Schedule</span>
  <span class="nav" style="left:815px">Testimonials</span>
  <span class="nav" style="left:925px">Blog</span>
  <i class="dot" style="left:991px"></i>
  <i class="dot" style="left:1024px"></i>
  <i class="dot" style="left:1056px"></i>
  <svg class="abs" style="left:1099px;top:53px" width="16" height="16" viewBox="0 0 16 16" fill="none" stroke="#444" stroke-width="1.6"><circle cx="6.5" cy="6.5" r="5"/><path d="M10.5 10.5 15 15"/></svg>
  <div class="ph" role="img" aria-label="Portrait of the coach in a white blazer, arms crossed" style="left:87px;top:135px;width:336px;height:548px;background:linear-gradient(180deg,#d9d4cf 0%,#eae7e3 55%,#cfcac4 100%);border-radius:160px 160px 0 0"></div>
  <h1 class="serif">“Always Push Yourself to the Next Level”</h1>
  <p>If you are not willing to risk the usual, you will have to settle for the ordinary. I'm here to help and share my story.</p>
  <a class="btn btn-dark" style="left:513px;top:500px;width:185px;height:54px">Get Free Session</a>
  <div class="ph" role="img" aria-label="Handwritten signature" style="left:730px;top:505px;width:193px;height:44px;background:linear-gradient(90deg,rgba(60,60,60,.12),rgba(60,60,60,.05))"></div>
</section>

<section class="story">
  <div class="abs label" style="left:87px;top:854px">My Story</div>
  <h2 class="abs serif" style="left:87px;top:880px">Hello, I’m Maren<br>Holt</h2>
  <p class="abs" style="left:87px;top:1010px">Lorem ipsum dolor sit amet, consectetur adipiscing elit. Suspendisse sed interdum leo. Sed pretium eleifend risus nec sagittis. Quisque laoreet purus aliquam, mattis metus vitae, ornare tellus. Curabitur bibendum facilisis mauris, sed varius enim pretium ut. Mauris bibendum ex erat, nec volutpat est vulputate non.</p>
  <a class="btn btn-outline" style="left:87px;top:1150px;width:186px;height:58px">Read My Story</a>
  <div class="ph" style="left:779px;top:888px;width:334px;height:381px;background:var(--green)"></div>
  <div class="ph" role="img" aria-label="Smiling coach in a white shirt leaning against a tree trunk" style="left:683px;top:798px;width:413px;height:456px;background:linear-gradient(135deg,#7b6a5e 0%,#a59384 45%,#e8e4df 70%,#5d5048 100%)"></div>
</section>

<section class="services">
  <div class="band-green"></div>
  <div class="abs label" style="left:87px;top:1497px;color:var(--white)">My Services</div>
  <h2 class="abs serif" style="left:87px;top:1520px;font-size:44px;color:var(--white)">My Most Beloved Services</h2>
  <a class="btn" style="left:927px;top:1498px;width:186px;height:58px;border:2px solid var(--white);color:var(--white)">View All Services</a>

  <article class="card" style="left:87px;top:1602px;width:323px;height:536px">
    <div class="ph" role="img" aria-label="Young woman listening during a one-to-one session" style="left:0;top:0;width:323px;height:258px;background:linear-gradient(135deg,#4a3a32,#b9b4b6 60%,#dedde3)"></div>
    <span class="tag">One to One</span>
    <h3 class="abs serif svc-title" style="left:32px;top:290px">Personal Sessions and<br>Workshops</h3>
    <p class="abs small" style="left:32px;top:362px;width:260px">Lorem ipsum dolor sit amet, consectetur adipiscing elit. Suspendisse sed interdum leo.Sed pretium eleifend risus</p>
    <a class="btn btn-outline" style="left:32px;top:452px;width:126px;height:50px;font-size:11.5px">Enroll Now</a>
  </article>
  <article class="card" style="left:438px;top:1602px;width:324px;height:536px">
    <div class="ph" role="img" aria-label="Clipboard with caution note beside a cup of coffee on a pink desk" style="left:0;top:0;width:324px;height:258px;background:linear-gradient(135deg,#f3c5c0,#f7d9d4 55%,#efe6e0)"></div>
    <span class="tag">Public</span>
    <h3 class="abs serif svc-title" style="left:32px;top:290px">Public Program for<br>Individuals and Teams</h3>
    <p class="abs small" style="left:32px;top:362px;width:260px">Lorem ipsum dolor sit amet, consectetur adipiscing elit. Suspendisse sed interdum leo.Sed pretium eleifend risus</p>
    <a class="btn btn-outline" style="left:32px;top:452px;width:126px;height:50px;font-size:11.5px">Enroll Now</a>
  </article>
  <article class="card" style="left:790px;top:1602px;width:323px;height:536px">
    <div class="ph" role="img" aria-label="Hands using a tablet and writing notes at a wooden desk" style="left:0;top:0;width:323px;height:258px;background:linear-gradient(135deg,#d8d4cf,#8c8580 50%,#e7e3de)"></div>
    <span class="tag">Online</span>
    <h3 class="abs serif svc-title" style="left:32px;top:290px">Learn Secrets to Peak<br>Performance</h3>
    <p class="abs small" style="left:32px;top:362px;width:260px">Lorem ipsum dolor sit amet, consectetur adipiscing elit. Suspendisse sed interdum leo.Sed pretium eleifend risus</p>
    <a class="btn btn-outline" style="left:32px;top:452px;width:126px;height:50px;font-size:11.5px">Enroll Now</a>
  </article>
</section>

<section class="schedule">
  <div class="abs label" style="left:0;width:1200px;text-align:center;top:2254px">Schedule</div>
  <h2 class="abs serif" style="left:0;width:1200px;text-align:center;top:2275px;font-size:46px">Upcoming Schedule</h2>
  <article class="card" style="left:87px;top:2360px;width:236px;height:323px">
    <div class="ph" role="img" aria-label="Line icon of a person with goal arrows" style="left:26px;top:34px;width:74px;height:74px;background:var(--mint);border-radius:8px"></div>
    <svg class="abs" style="left:26px;top:138px" width="14" height="14" viewBox="0 0 14 14" fill="none" stroke="#03a98d" stroke-width="1.4"><rect x="1" y="2.5" width="12" height="10.5"/><path d="M1 6h12M4 1v3M10 1v3"/></svg>
    <span class="abs" style="left:50px;top:139px;font-size:10.5px;color:var(--green)">July 30, 2022 | 12:00 PM</span>
    <h3 class="abs serif" style="left:26px;top:168px;font-size:22px;font-weight:500">Ut lobortis in nunc<br>velauctor.</h3>
    <a class="abs link" style="left:26px;top:257px">View Details</a>
  </article>
  <article class="card" style="left:348px;top:2360px;width:237px;height:323px">
    <div class="ph" role="img" aria-label="Line icon of a hand holding a person with a heart" style="left:26px;top:34px;width:74px;height:74px;background:var(--mint);border-radius:8px"></div>
    <svg class="abs" style="left:26px;top:138px" width="14" height="14" viewBox="0 0 14 14" fill="none" stroke="#03a98d" stroke-width="1.4"><rect x="1" y="2.5" width="12" height="10.5"/><path d="M1 6h12M4 1v3M10 1v3"/></svg>
    <span class="abs" style="left:50px;top:139px;font-size:10.5px;color:var(--green)">July 30, 2022 | 12:00 PM</span>
    <h3 class="abs serif" style="left:26px;top:168px;font-size:22px;font-weight:500">Ut lobortis in nunc<br>velauctor.</h3>
    <a class="abs link" style="left:26px;top:257px">View Details</a>
  </article>
  <article class="card" style="left:611px;top:2360px;width:237px;height:323px">
    <div class="ph" role="img" aria-label="Line icon of a coach presenting to a group" style="left:26px;top:34px;width:74px;height:74px;background:var(--mint);border-radius:8px"></div>
    <svg class="abs" style="left:26px;top:138px" width="14" height="14" viewBox="0 0 14 14" fill="none" stroke="#03a98d" stroke-width="1.4"><rect x="1" y="2.5" width="12" height="10.5"/><path d="M1 6h12M4 1v3M10 1v3"/></svg>
    <span class="abs" style="left:50px;top:139px;font-size:10.5px;color:var(--green)">July 30, 2022 | 12:00 PM</span>
    <h3 class="abs serif" style="left:26px;top:168px;font-size:22px;font-weight:500">Ut lobortis in nunc<br>velauctor.</h3>
    <a class="abs link" style="left:26px;top:257px">View Details</a>
  </article>
  <article class="card" style="left:875px;top:2360px;width:237px;height:323px">
    <div class="ph" role="img" aria-label="Line icon of a counsellor with a heart" style="left:26px;top:34px;width:74px;height:74px;background:var(--mint);border-radius:8px"></div>
    <svg class="abs" style="left:26px;top:138px" width="14" height="14" viewBox="0 0 14 14" fill="none" stroke="#03a98d" stroke-width="1.4"><rect x="1" y="2.5" width="12" height="10.5"/><path d="M1 6h12M4 1v3M10 1v3"/></svg>
    <span class="abs" style="left:50px;top:139px;font-size:10.5px;color:var(--green)">July 30, 2022 | 12:00 PM</span>
    <h3 class="abs serif" style="left:26px;top:168px;font-size:22px;font-weight:500">Ut lobortis in nunc<br>velauctor.</h3>
    <a class="abs link" style="left:26px;top:257px">View Details</a>
  </article>
</section>

<section class="testimonials">
  <div class="band-mint"></div>
  <div class="abs label" style="left:87px;top:2912px">Cients Testimonials</div>
  <h2 class="abs serif" style="left:87px;top:2938px;font-size:46px">Satisfied Users Over<br>The Globel</h2>
  <p class="abs" style="left:87px;top:3064px;width:460px;font-size:13px;line-height:1.75">Lorem ipsum dolor sit amet, consectetur adipiscing elit. Suspendisse sed interdum leo. Sed pretium eleifend risus nec sagittis. Quisque laoreet purus aliquam</p>

  <div class="quote" style="left:613px;top:2913px">
    <svg width="100" height="18" viewBox="0 0 100 18" fill="#03a98d"><g id="st"><polygon points="9,0 11.6,6 18,6.5 13.1,10.6 14.6,17 9,13.6 3.4,17 4.9,10.6 0,6.5 6.4,6"/></g><use href="#st" x="20"/><use href="#st" x="40"/><use href="#st" x="60"/><use href="#st" x="80"/></svg>
    <p style="margin-top:10px">Donec pellentesque laoreet quam. Praesent maximus ligula ornare imperdiet placerat. Donec ut finibus elit. Nulla consectetur convallis suscipit.</p>
  </div>
  <div class="avatar" role="img" aria-label="Client portrait" style="left:653px;top:3182px"></div>
  <div class="abs" style="left:727px;top:3189px;font-size:14px;font-weight:500;color:var(--ink)">Nora Bell</div>
  <div class="abs" style="left:727px;top:3212px;font-size:10.5px;color:var(--green)">CEO at Fernline</div>

  <div class="quote" style="left:877px;top:2913px">
    <svg width="100" height="18" viewBox="0 0 100 18" fill="#03a98d"><use href="#st"/><use href="#st" x="20"/><use href="#st" x="40"/><use href="#st" x="60"/><use href="#st" x="80"/></svg>
    <p style="margin-top:10px">Donec pellentesque laoreet quam. Praesent maximus ligula ornare imperdiet placerat. Donec ut finibus elit. Nulla consectetur convallis suscipit.</p>
  </div>
  <div class="avatar" role="img" aria-label="Client portrait" style="left:916px;top:3182px;background:linear-gradient(135deg,#d7b5a8,#8a5d4c)"></div>
  <div class="abs" style="left:990px;top:3189px;font-size:14px;font-weight:500;color:var(--ink)">Nora Bell</div>
  <div class="abs" style="left:990px;top:3212px;font-size:10.5px;color:var(--green)">CEO at Fernline</div>
</section>

<section class="blog">
  <div class="abs label" style="left:0;width:1200px;text-align:center;top:3468px">Our Blog</div>
  <h2 class="abs serif" style="left:0;width:1200px;text-align:center;top:3488px;font-size:46px">Latest News &amp; Updates</h2>

  <article class="card" style="left:87px;top:3571px;width:323px;height:454px;border:1px solid var(--line);box-shadow:none">
    <div class="ph" role="img" aria-label="Notebook asking what do you want from life, beside a coffee cup" style="left:0;top:0;width:321px;height:246px;background:linear-gradient(135deg,#3b2a22,#e6e4df 45%,#f2f1ee)"></div>
    <div class="badge" style="left:224px;top:216px">31<span>JULY</span></div>
    <svg class="abs" style="left:30px;top:286px" width="14" height="14" viewBox="0 0 14 14" fill="#03a98d"><circle cx="7" cy="4" r="3.2"/><path d="M1 14c0-3.6 2.7-5.5 6-5.5s6 1.9 6 5.5z"/></svg>
    <span class="abs" style="left:52px;top:284px;font-size:13.5px;color:var(--green)">By Admin</span>
    <h3 class="abs serif" style="left:30px;top:322px;font-size:20px;font-weight:500">Lorem ipsum dolor sit amet,<br>consectetur adipiscing</h3>
    <a class="abs link" style="left:30px;top:398px">Read More</a>
  </article>
  <article class="card" style="left:438px;top:3571px;width:324px;height:454px;border:1px solid var(--line);box-shadow:none">
    <div class="ph" role="img" aria-label="Woman in a coaching conversation with a man in a bright room" style="left:0;top:0;width:322px;height:246px;background:linear-gradient(135deg,#e9e6e1,#c4b7a8 50%,#2f3d55)"></div>
    <div class="badge" style="left:224px;top:216px">31<span>JULY</span></div>
    <svg class="abs" style="left:30px;top:286px" width="14" height="14" viewBox="0 0 14 14" fill="#03a98d"><circle cx="7" cy="4" r="3.2"/><path d="M1 14c0-3.6 2.7-5.5 6-5.5s6 1.9 6 5.5z"/></svg>
    <span class="abs" style="left:52px;top:284px;font-size:13.5px;color:var(--green)">By Admin</span>
    <h3 class="abs serif" style="left:30px;top:322px;font-size:20px;font-weight:500">Lorem ipsum dolor sit amet,<br>consectetur adipiscing</h3>
    <a class="abs link" style="left:30px;top:398px">Read More</a>
  </article>
  <article class="card" style="left:790px;top:3571px;width:323px;height:454px;border:1px solid var(--line);box-shadow:none">
    <div class="ph" role="img" aria-label="Runner climbing outdoor steps painted with a motivational phrase" style="left:0;top:0;width:321px;height:246px;background:linear-gradient(180deg,#e7c9b6,#c99a95 50%,#b37f86)"></div>
    <div class="badge" style="left:224px;top:216px">31<span>JULY</span></div>
    <svg class="abs" style="left:30px;top:286px" width="14" height="14" viewBox="0 0 14 14" fill="#03a98d"><circle cx="7" cy="4" r="3.2"/><path d="M1 14c0-3.6 2.7-5.5 6-5.5s6 1.9 6 5.5z"/></svg>
    <span class="abs" style="left:52px;top:284px;font-size:13.5px;color:var(--green)">By Admin</span>
    <h3 class="abs serif" style="left:30px;top:322px;font-size:20px;font-weight:500">Lorem ipsum dolor sit amet,<br>consectetur adipiscing</h3>
    <a class="abs link" style="left:30px;top:398px">Read More</a>
  </article>
</section>

<section class="newsletter">
  <div class="ph" role="img" aria-label="Woman with open arms in a sunlit field at sunset" style="left:0;top:4134px;width:1200px;height:395px;background:linear-gradient(90deg,#fbf6ef 0%,#f6ead8 45%,#e9c99c 75%,#c79a6a 100%)"></div>
  <div class="abs label" style="left:87px;top:4254px">Keep up to date with advantage</div>
  <h2 class="abs serif" style="left:87px;top:4274px;font-size:46px">Subscribe to Our Newsletter</h2>
  <div class="abs" style="left:87px;top:4352px;width:294px;height:65px;background:var(--white);font-size:12px;color:#666;padding:24px 24px">Enter Email</div>
  <a class="btn btn-dark" style="left:381px;top:4352px;width:119px;height:65px;font-size:11.5px">Subscribe</a>
</section>

<footer>
  <div class="abs" style="left:87px;top:4680px;display:flex;align-items:center;gap:8px;font-size:14px;font-weight:500;color:var(--ink)"><i style="width:24px;height:24px;border:2px solid var(--green);border-radius:50%;display:block"></i>BRIGHT SUMMIT</div>
  <div class="abs" style="left:87px;top:4755px;font-size:12px;color:#333">hello@brightsummit-mail.com</div>
  <div class="abs" style="left:87px;top:4792px;font-size:12px;color:#333">(555) 014 2290</div>
  <div class="abs" style="left:87px;top:4830px;font-size:12px;color:#333">Enter your address here</div>

  <a class="foot-link" style="left:533px;top:4643px">My Story</a>
  <a class="foot-link" style="left:533px;top:4691px">My Schedule</a>
  <a class="foot-link" style="left:533px;top:4739px">Services</a>
  <a class="foot-link" style="left:700px;top:4643px">Testimonials</a>
  <a class="foot-link" style="left:700px;top:4691px">News</a>
  <a class="foot-link" style="left:700px;top:4739px">Contact</a>
  <a class="foot-link" style="left:865px;top:4643px">FAQs</a>
  <a class="foot-link" style="left:865px;top:4691px">T &amp; C</a>

  <i class="social" style="left:966px"></i>
  <i class="social" style="left:1018px"></i>
  <i class="social" style="left:1072px"></i>

  <div class="abs" style="left:87px;top:4895px;font-size:11.5px;color:#555">Copyright 2022.All right reserved.</div>
  <div class="abs" style="left:956px;top:4895px;font-size:11.5px;color:#555">Privacy Policy</div>
  <div class="abs" style="left:1066px;top:4895px;font-size:11.5px;color:#555">Sitemap</div>
</footer>

</body>
</html>
```